Business Card Design

I am a new realtor. To stand out from the other 25 realtors in my firm I need a card that will stand out. I am the youngest realtor here, so I want something to reflect that. Something different, as opposed to the same old traditional, boring cards everyone else has. It of course needs to have my picture which I will download for you ( I included a black and white option as well as color. Either are fine) and you can crop it or do whatever you need to make it look the best. Our company colors are red and white. These don't have to be the only colors on the card, but the red especially needs to be a focal color. I like a clean, stream-line look while still eye-catching. Not over the top busy.
While I do have to provide the company logo, I am a contractor. Therefore, I want the focus on me and my information.
Industry/Entity Type
Realtor
Contact Information for Business Card
Marisa Quillon
Realtor (this needs the realtor logo which has the R in the circle at the end)
(office)555.318.4406
(cell) 555.892.6035
Mquillon@brv-homegroup.example
It will also need our company logo which I will download and send
Requirements
Nice to have
- I like the look of the foil or metallic. However, this is definitely not a requirement

```html
<!DOCTYPE html>
<html lang="en">
<head>
<meta charset="utf-8">
<title>Marisa Quillon – Realtor Business Card</title>
<link rel="stylesheet" href="https://fonts.googleapis.com/css2?family=Roboto+Condensed:wght@400;700&display=swap">
<style>
  :root {
    --brand-red: #e00000;
    --brand-red-deep: #b80000;
    --shadow-red: #8a0000;
    --paper-white: #f6f6f4;
    --ink-white: #ffffff;
    --photo-light: #d9d9d9;
    --photo-dark: #4a4a4a;
  }
  html, body {
    margin: 0;
    padding: 0;
    width: 1200px;
    height: 702px;
    overflow: hidden;
    background: var(--paper-white);
  }
  .business-card {
    position: relative;
    width: 1200px;
    height: 702px;
    overflow: hidden;
    font-family: "Roboto Condensed", "Arial Narrow", sans-serif;
    color: var(--ink-white);
    background: var(--paper-white);
  }
  .card-shapes {
    position: absolute;
    inset: 0;
  }
  .brokerage-name {
    position: absolute;
    left: 72px;
    top: 72px;
    width: 300px;
    font-weight: 400;
    font-size: 30px;
    line-height: 1.25;
    letter-spacing: 1px;
    text-align: center;
    color: var(--ink-white);
  }
  .brokerage-name .tagline {
    display: block;
    font-size: 24px;
    letter-spacing: 0.5px;
    margin-top: 6px;
  }
  .agent-block {
    position: absolute;
    right: 492px;
    top: 262px;
    text-align: right;
  }
  .agent-name {
    margin: 0;
    font-weight: 700;
    font-size: 84px;
    line-height: 1;
    letter-spacing: -1.5px;
    white-space: nowrap;
  }
  .agent-title {
    position: absolute;
    left: 276px;
    top: 378px;
    width: 432px;
    height: 38px;
  }
  .agent-title svg {
    position: absolute;
    inset: 0;
  }
  .agent-title span {
    position: absolute;
    left: 150px;
    top: -3px;
    font-weight: 700;
    font-size: 42px;
    line-height: 44px;
    color: var(--brand-red);
  }
  .contact-list {
    position: absolute;
    right: 492px;
    top: 448px;
    margin: 0;
    padding: 0;
    list-style: none;
    text-align: right;
    font-weight: 400;
    font-size: 44px;
    line-height: 1;
  }
  .contact-list li {
    display: flex;
    justify-content: flex-end;
    align-items: center;
    gap: 18px;
    height: 52px;
    margin-bottom: 14px;
    white-space: nowrap;
  }
  .contact-list .contact-email {
    font-size: 40px;
    letter-spacing: -0.5px;
  }
  .contact-icon {
    width: 40px;
    height: 48px;
  }
</style>
</head>
<body>
<main class="business-card">
  <svg class="card-shapes" width="1200" height="702" viewBox="0 0 1200 702" aria-hidden="false">
    <defs>
      <linearGradient id="red-field" x1="0" y1="0" x2="0" y2="1">
        <stop offset="0" stop-color="#e60000"/>
        <stop offset="1" stop-color="#d40000"/>
      </linearGradient>
      <linearGradient id="portrait-tone" x1="0" y1="0" x2="1" y2="1">
        <stop offset="0" stop-color="var(--photo-light)"/>
        <stop offset="0.55" stop-color="#8c8c8c"/>
        <stop offset="1" stop-color="var(--photo-dark)"/>
      </linearGradient>
      <linearGradient id="fold-shadow" x1="0" y1="0" x2="1" y2="1">
        <stop offset="0" stop-color="#5c0000"/>
        <stop offset="1" stop-color="var(--shadow-red)"/>
      </linearGradient>
    </defs>

    <!-- red field -->
    <polygon class="red-field" points="0,0 719,0 885,288 929,702 0,702" fill="url(#red-field)"/>

    <!-- faint sketch area -->
    <rect class="sketch-area" x="60" y="230" width="860" height="440" fill="#cf0000" opacity="0.35"
          role="img" aria-label="Faint pencil sketch of a house and trees"/>

    <!-- portrait -->
    <polygon class="portrait" points="719,0 1200,0 1200,702 929,702 885,288" fill="url(#portrait-tone)"
             role="img" aria-label="Black and white portrait photo of the realtor"/>

    <!-- dark folded triangle -->
    <polygon class="fold-triangle-shadow" points="584,150 719,0 893,296" fill="#3a0000" opacity="0.35"/>
    <polygon class="fold-triangle" points="592,144 719,0 885,288" fill="url(#fold-shadow)"/>
  </svg>

  <div class="brokerage-name">
    HARLOW VANCE<br>&amp; COMPANY
    <span class="tagline">Real Estate Brokerage</span>
  </div>

  <div class="agent-block">
    <h1 class="agent-name">Marisa Quillon</h1>
  </div>

  <div class="agent-title">
    <svg width="432" height="38" viewBox="0 0 432 38" aria-hidden="true">
      <polygon points="0,0 432,0 432,38 0,38 22,19" fill="#ffffff"/>
    </svg>
    <span>Realtor</span>
  </div>

  <ul class="contact-list">
    <li class="contact-office">
      <svg class="contact-icon" viewBox="0 0 40 48" aria-label="Office phone">
        <rect x="1" y="2" width="10" height="44" rx="4" fill="#ffffff"/>
        <rect x="13" y="4" width="25" height="40" rx="3" fill="none" stroke="#ffffff" stroke-width="3"/>
        <rect x="18" y="9" width="15" height="8" fill="#ffffff"/>
        <g fill="#ffffff">
          <rect x="18" y="21" width="4" height="4"/><rect x="24" y="21" width="4" height="4"/><rect x="30" y="21" width="4" height="4"/>
          <rect x="18" y="28" width="4" height="4"/><rect x="24" y="28" width="4" height="4"/><rect x="30" y="28" width="4" height="4"/>
          <rect x="18" y="35" width="4" height="4"/><rect x="24" y="35" width="4" height="4"/><rect x="30" y="35" width="4" height="4"/>
        </g>
      </svg>
      <span>555.318.4406</span>
    </li>
    <li class="contact-cell">
      <svg class="contact-icon" viewBox="0 0 40 48" aria-label="Cell phone">
        <rect x="8" y="2" width="24" height="44" rx="4" fill="none" stroke="#ffffff" stroke-width="3.5"/>
        <line x1="9" y1="36" x2="31" y2="36" stroke="#ffffff" stroke-width="3"/>
        <circle cx="20" cy="41" r="2" fill="#ffffff"/>
      </svg>
      <span>555.892.6035</span>
    </li>
    <li class="contact-email">Mquillon@brv-homegroup.example</li>
  </ul>
</main>
</body>
</html>
```